Local Finance and Insurance Advising Company from Switzerland needs an impressive banner design.

I am looking for an impressive Banner Design, I need this Banner for Facebook, LinkedIn, YouTube & Google.

I am Advising all kind of peoples who are living here in Switzerland. Young, middle age and old people. People who want to go study, people who are planning to create a family, old people who are, or going to retire. Expatriates who want to leave Switzerland to live in another country, expatriates who are coming to Switzerland. Peoples who ant to build their own business up. All kind of financial, insurance and pension planning's.

The Company Name is: Alpine Counsel
Our slogen / heading is: Clear Counsel, no Pitch

The Company logo can be used for the banner, but I would preffer to have the banner without logo, as the logo will be already in a another field on the social networks.

Since the first impression is the most important, this project is really important to me. I am ready to realize further projects with the one who can create the perfect banner who hits the point as described. I am a start-up company, everything is still on beginning and still much has to be done.

Target Market(s)

private clients

Requirements
Must have
• The banner should give the impression of happiness, safeness, health and freedom. Empowering people and creating freedom lifestyles.
Should not have
• I do not want that the banner looks like we are some kind of broker who is just selling some kind of insurances.

```html
<!DOCTYPE html>
<html lang="en">
<head>
<meta charset="utf-8">
<title>Alpine Counsel – Social Banners</title>
<link href="https://fonts.googleapis.com/css2?family=Antonio:wght@400;700&display=swap" rel="stylesheet">
<style>
  :root {
    --board: #efefef;
    --red: #d9172e;
    --red-deep: #c8122a;
    --ink-purple: #5a4b6b;
    --white: #ffffff;
    --paper: #f1f0ee;
    --cream: #fdf8ec;
    --mint: #cfe6d3;
    --skin: #e8cbb6;
    --stone: #bdbdbd;
    --sunset: #dc9f62;
  }
  * { margin: 0; padding: 0; box-sizing: border-box; }
  html, body {
    width: 1200px; height: 1178px; overflow: hidden;
    background: var(--board);
    font-family: "Antonio", "Arial Narrow", sans-serif;
  }
  .board { position: relative; width: 1200px; height: 1178px; }

  .banner {
    position: absolute; overflow: hidden;
    box-shadow: 0 14px 30px rgba(0,0,0,0.12);
  }
  .banner svg.shapes { position: absolute; inset: 0; }
  .photo { position: absolute; }

  /* Banner one: family */
  .banner--family {
    left: 121px; top: 112px; width: 958px; height: 401px;
    background: linear-gradient(180deg, #f3f3f2 0%, #ecebea 100%);
  }
  .photo--family {
    left: 0; top: 70px; width: 560px; height: 331px;
    background:
      linear-gradient(90deg, rgba(243,243,242,0) 70%, #f1f1f0 100%),
      linear-gradient(90deg, var(--mint) 0%, #ead6c4 35%, #f1e4da 58%, #f4efea 80%);
    border-radius: 140px 160px 0 0;
  }
  .photo--rock {
    left: 535px; top: 220px; width: 250px; height: 181px;
    background: linear-gradient(180deg, #d8d8d8 0%, var(--stone) 55%, #d2d2d2 100%);
    border-radius: 90px 70px 0 0;
    opacity: 0.8;
  }
  .headline--family {
    position: absolute; left: 522px; top: 82px;
    color: var(--red); line-height: 1; white-space: nowrap;
  }
  .headline--family .line-main { display: block; font-weight: 700; font-size: 58px; letter-spacing: 0.3px; }
  .headline--family .line-sub {
    display: block; font-weight: 400; font-size: 58px; margin-top: 6px;
    color: transparent; -webkit-text-stroke: 1.4px var(--red); letter-spacing: 1px;
  }
  .brand--family {
    position: absolute; left: 812px; top: 352px;
    color: var(--white); font-weight: 700; font-size: 20px; letter-spacing: 1px;
    text-transform: uppercase; white-space: nowrap;
  }

  /* Banner two: freedom */
  .banner--freedom {
    left: 123px; top: 635px; width: 954px; height: 409px;
    background: var(--cream);
  }
  .photo--sunset {
    left: 0; right: 0; bottom: 0; height: 120px;
    background: linear-gradient(180deg, rgba(253,248,236,0) 0%, #eec18b 45%, var(--sunset) 100%);
  }
  .photo--woman {
    left: 560px; top: 30px; width: 370px; height: 379px;
    background: linear-gradient(180deg, #f1d6c8 0%, #f6e7dd 45%, #c8b3a6 80%, #6e6a82 100%);
    border-radius: 180px 180px 0 0;
    opacity: 0.85;
  }
  .brand--freedom {
    position: absolute; left: 0; width: 596px; top: 80px; text-align: center;
    color: var(--red); font-weight: 700; font-size: 30px; letter-spacing: 2px;
    text-transform: uppercase; white-space: nowrap;
  }
  .headline--freedom {
    position: absolute; left: 0; top: 168px; width: 596px; text-align: center;
    line-height: 1; font-weight: 400; white-space: nowrap;
  }
  .headline--freedom .line-main { display: block; color: var(--ink-purple); font-size: 72px; }
  .headline--freedom .line-sub { display: block; color: var(--red); font-size: 48px; margin-top: 10px; }
</style>
</head>
<body>
<main class="board">

  <section class="banner banner--family">
    <div class="photo photo--family" role="img" aria-label="Photo of a laughing family: grandparents, a young mother and a baby"></div>
    <div class="photo photo--rock" role="img" aria-label="Faded photo of a rocky outcrop with a small flag above a waterfall"></div>
    <svg class="shapes" width="958" height="401" viewBox="0 0 958 401" aria-hidden="true">
      <path d="M0 0 H124 C62 22 16 70 0 112 Z" fill="var(--red)"/>
      <path d="M921 0 H958 V401 H701 C842 342 912 205 921 0 Z" fill="var(--red-deep)"/>
    </svg>
    <h2 class="headline--family">
      <span class="line-main">CLEAR COUNSEL,</span>
      <span class="line-sub">NO PITCH</span>
    </h2>
    <p class="brand--family">Alpine Counsel</p>
  </section>

  <section class="banner banner--freedom">
    <div class="photo photo--sunset" role="img" aria-label="Sunlit evening sky over a blurred line of trees"></div>
    <div class="photo photo--woman" role="img" aria-label="Photo of a young woman with arms spread wide, enjoying the sun"></div>
    <svg class="shapes" width="954" height="409" viewBox="0 0 954 409" aria-hidden="true">
      <path d="M0 0 H298 C168 20 40 62 0 126 Z" fill="var(--red)"/>
      <path d="M954 324 V409 H755 C852 396 930 370 954 324 Z" fill="var(--red)"/>
    </svg>
    <p class="brand--freedom">Alpine Counsel</p>
    <h2 class="headline--freedom">
      <span class="line-main">CLEAR COUNSEL,</span>
      <span class="line-sub">NO PITCH</span>
    </h2>
  </section>

</main>
</body>
</html>
```